Vintage themed home decor Shopify store needs sales promotion banner ads

"Quill & Lantern Goods" is an Australian based lifestyle home decor store that sells vintage, retro and antique relic replicas and reproduction items online to their local customers Australia wide.

We need banner ads for our store home page slider that promotes our unique products, new stock arrival and calls store visitors to to buy from our different product collections.

We anticipate that we will need multiple banner ads, primarily for the following product collections:
1. Sundials & Compass
2. Airplane models
3. Magnifying glass
4. Clocks & Watches

Banners could also be generic with generic discount coupon promotions.

Banners should be based around the theme of our store and products which gives a sense of colonial / vintage lifestyle and that they compliment the colour & theme of the store.

Banner Size: 1600 x 800 px

Please find attached some samples of the types of banner ads we have in mind and also our logo. Product images can be supplied if they are required to be used in the ads.

Website URL: https://quillandlanterngoods.example

Target Market(s)

mostly Males aged between 35-65.
Products ideally for man-cave & office decor.

Industry/Entity Type

Home And Garden

Font styles to use
Serif
Decorative
Script

Requirements
Must have
• some product images
Nice to have
• lifestyle shots.
• blank space to insert for a coupon code
Should not have
• caricatures & cartoon

```html
<!DOCTYPE html>
<html lang="en">
<head>
<meta charset="utf-8">
<title>Quill &amp; Lantern Goods – Special Offer Banner</title>
<link href="https://fonts.googleapis.com/css2?family=Libre+Baskerville:wght@400;700&family=Oswald:wght@300&family=Montserrat:wght@400;700&display=swap" rel="stylesheet">
<style>
  :root{
    --page-bg:#f2efe9;
    --parchment-light:#e6ddcc;
    --parchment-dark:#cbbfa9;
    --ink:#111111;
    --headline:#3a0d0d;
    --card:#ffffff;
    --offer-red:#d42b37;
    --button:#f04e0f;
    --field-border:#2a2a2a;
    --placeholder:#6b6b6b;
  }
  *{box-sizing:border-box;margin:0;padding:0}
  html,body{width:1200px;height:1200px;overflow:hidden;background:var(--page-bg)}
  .banner{
    position:absolute;left:0;top:300px;width:1200px;height:600px;overflow:hidden;
    background:radial-gradient(ellipse at 50% 45%,var(--parchment-light) 0%,#ddd3c0 55%,var(--parchment-dark) 100%);
  }
  .map-texture{position:absolute;inset:0;
    background:radial-gradient(circle at 82% 10%,rgba(190,175,145,.35) 0,rgba(190,175,145,0) 30%),
               radial-gradient(circle at 20% 80%,rgba(170,155,125,.25) 0,rgba(170,155,125,0) 35%);}
  .product{position:absolute;border-radius:18px}
  .product--airplane{left:14px;top:36px;width:331px;height:117px;background:linear-gradient(90deg,#d9a928,#e8c14a 50%,#b98b1e)}
  .product--binoculars{left:29px;top:183px;width:104px;height:216px;background:linear-gradient(180deg,#5a4a30,#9a8458 40%,#7c6a48)}
  .product--record-player{left:28px;top:426px;width:136px;height:138px;background:linear-gradient(160deg,#8a3b1e,#6a2a14)}
  .product--gramophone{left:196px;top:348px;width:127px;height:210px;background:linear-gradient(170deg,#d8b860,#b08a36 60%,#6e4b22)}
  .product--diving-helmet{left:869px;top:23px;width:91px;height:108px;background:radial-gradient(circle at 45% 40%,#c98a5a,#8a5233 70%)}
  .product--sundial{left:1017px;top:32px;width:121px;height:123px;border-radius:50%;background:radial-gradient(circle,#9a8450,#6b5a32 70%)}
  .product--sailboat{left:964px;top:192px;width:208px;height:210px;background:linear-gradient(180deg,#f1eee7,#dcd6c8 70%,#2a2420)}
  .product--race-car{left:907px;top:430px;width:247px;height:154px;background:linear-gradient(180deg,#c9ccd0,#8c9095 60%,rgba(140,144,149,.3))}
  .brand{position:absolute;left:367px;top:36px;width:480px;text-align:center}
  .brand__name{font-family:"Libre Baskerville",serif;font-weight:400;font-size:40px;color:var(--ink);line-height:1.4;padding-top:18px}
  .brand__tagline{font-family:"Oswald",sans-serif;font-weight:300;font-size:21px;color:var(--ink);margin-top:6px;letter-spacing:-.2px}
  .offer-card{position:absolute;left:353px;top:176px;width:493px;height:349px;background:var(--card);box-shadow:0 2px 10px rgba(0,0,0,.12)}
  .offer-card__headline{position:absolute;top:40px;left:0;right:0;text-align:center;font-family:"Libre Baskerville",serif;font-size:21px;line-height:27px;color:var(--headline)}
  .offer-card__stamp{position:absolute;left:184px;top:114px;width:125px;height:125px;border-radius:50%;background:radial-gradient(circle,#e04350,var(--offer-red) 70%)}
  .promo-form{position:absolute;left:52px;top:262px;width:397px;height:43px;border:1.5px solid var(--field-border);border-radius:5px;display:flex;overflow:hidden}
  .promo-form__field{flex:1;display:flex;align-items:center;padding-left:22px;font-family:"Montserrat",sans-serif;font-size:15px;color:var(--placeholder)}
  .promo-form__button{width:122px;background:var(--button);display:flex;align-items:center;justify-content:center;font-family:"Montserrat",sans-serif;font-weight:700;font-size:15px;color:#fff}
</style>
</head>
<body>
  <section class="banner">
    <div class="map-texture" role="img" aria-label="Faded antique world map background"></div>
    <div class="product product--airplane" role="img" aria-label="Yellow vintage biplane model"></div>
    <div class="product product--binoculars" role="img" aria-label="Brass binoculars on a tripod stand"></div>
    <div class="product product--record-player" role="img" aria-label="Wooden retro record player"></div>
    <div class="product product--gramophone" role="img" aria-label="Brass horn gramophone"></div>
    <div class="product product--diving-helmet" role="img" aria-label="Copper diving helmet replica"></div>
    <div class="product product--sundial" role="img" aria-label="Brass sundial compass"></div>
    <div class="product product--sailboat" role="img" aria-label="Model sailing yacht on stand"></div>
    <div class="product product--race-car" role="img" aria-label="Silver vintage race car model"></div>

    <header class="brand">
      <div class="brand__name">Quill &amp; Lantern Goods</div>
      <div class="brand__tagline">The Best Vintage &amp; Antique Collectibles Online</div>
    </header>

    <div class="offer-card">
      <h1 class="offer-card__headline">Desigen your home with the<br>best vintage &amp; antique collection</h1>
      <div class="offer-card__stamp" role="img" aria-label="Red exclusive special offer stamp"></div>
      <div class="promo-form">
        <div class="promo-form__field">Enter promo code</div>
        <div class="promo-form__button">CLICK HERE</div>
      </div>
    </div>
  </section>
</body>
</html>
```